Sunny Doodles - Face Painting Company requires business card design

Hi,
I am wanting a business card design for a new business in Brisbane (Australia) called 'Sunny Doodles'. We are a childrens face painting company.

I want to communicate a corporate, simple and clean message through my business card, but also fun and relevant to children.

My company colours are black, yellow and purple, and at the moment I am running with a "cheeky smile" type theme, along the lines of the Marlow Fox (Tobin and the Glass Kite).

I want this to look Corporate, clean and simple. On the back I would like to see some creative flair with a border or background design, perhaps in white or another colour.

• Front:
Sunny Doodles
Face Painting Designs

Back:
Hana Melrose
Artist
0432 918 246
hana@sunnydoodles.com.au
www.sunnydoodles.com.au
• Attached is the banner which i had made, the business card should go along with this type of theme.
I would like to use the colours Yellow, Black and Purple. Purple should be used in a miniml way, with yellow and black as the main colours.
I want it to have a CORPORATE look.

A Playfull but readable text.

I would like a mix up of the colours on the back in the text.
Hana Melrose (black)
Artist(purple) etc.

```html
<!DOCTYPE html>
<html lang="en">
<head>
<meta charset="utf-8">
<title>Sunny Doodles – Business Card Phase 1</title>
<link rel="stylesheet" href="https://fonts.googleapis.com/css2?family=Roboto:wght@300;400&family=Source+Sans+3:ital,wght@0,400;0,600;0,700;1,600&display=swap">
<style>
  :root {
    --sheet: #ffffff;
    --title-blue: #2f5cc0;
    --rule-blue: #7f9be0;
    --card-yellow: #f6d900;
    --card-yellow-deep: #e9c400;
    --ink: #111111;
    --purple: #6b4ea3;
    --purple-soft: #b7a6d8;
    --label: #222222;
  }
  * { margin: 0; padding: 0; box-sizing: border-box; }
  html, body { width: 1200px; height: 661px; overflow: hidden; background: var(--sheet); }
  .sheet { position: relative; width: 1200px; height: 661px; font-family: "Source Sans 3", sans-serif; }

  .sheet-title {
    position: absolute; left: 38px; top: 100px;
    font-family: "Roboto", sans-serif; font-weight: 300;
    font-size: 28px; color: var(--title-blue); letter-spacing: 0.2px;
  }
  .sheet-rule {
    position: absolute; left: 38px; top: 166px; width: 847px; height: 1px;
    background: var(--rule-blue);
  }

  .card {
    position: absolute; top: 239px; height: 348px; overflow: hidden;
    background: var(--card-yellow);
  }
  .card--back { left: 38px; width: 535px; }
  .card--front { left: 620px; width: 538px; }

  .card-edge { position: absolute; top: 0; bottom: 0; width: 15px; background: var(--ink); }
  .card--back .card-edge { left: 0; }
  .card--front .card-edge { right: 0; width: 19px; }

  .back-artwork {
    position: absolute; inset: 0;
    background: radial-gradient(ellipse at 40% 45%, #eacb2a 0%, var(--card-yellow-deep) 45%, var(--card-yellow) 80%);
    opacity: 0.9;
  }

  .contact { position: absolute; left: 69px; top: 44px; color: var(--ink); }
  .contact-name { font-size: 25px; font-weight: 700; line-height: 1.1; }
  .contact-role { font-size: 19px; font-weight: 600; font-style: italic; color: var(--purple); margin-top: 2px; }
  .contact-line { font-size: 18px; font-weight: 400; margin-top: 0; line-height: 1; }
  .contact-line b { font-weight: 700; }
  .contact-phone { margin-top: 32px; }
  .contact-email { margin-top: 17px; }
  .contact-web { margin-top: 18px; font-size: 20px; font-weight: 700; }

  .back-brand { position: absolute; right: 28px; bottom: 52px; display: flex; align-items: center; gap: 8px; }
  .brand-dot { width: 22px; height: 22px; border-radius: 50%; background: var(--purple); }
  .back-brand-name { font-size: 30px; font-weight: 700; line-height: 0.95; color: var(--ink); text-align: center; }
  .back-tagline { position: absolute; right: 24px; bottom: 14px; font-size: 17px; font-weight: 700; color: var(--ink); }

  .photo-strip { position: absolute; left: 0; top: 0; width: 69px; height: 100%; display: flex; flex-direction: column; gap: 3px; background: var(--ink); }
  .photo { flex: 1; }
  .photo--one { background: linear-gradient(160deg, #8a5a8e, #c98a6e); }
  .photo--two { background: linear-gradient(160deg, #d9782a, #8a3d1c); }
  .photo--three { background: linear-gradient(160deg, #3d6ec2, #b84a6a); }

  .front-tagline { position: absolute; left: 90px; top: 30px; font-size: 21px; font-weight: 700; color: var(--ink); }
  .front-brand { position: absolute; left: 120px; top: 92px; width: 320px; display: flex; flex-direction: column; align-items: center; }
  .front-brand-name { font-size: 86px; font-weight: 700; line-height: 0.92; color: var(--ink); text-align: center; }
  .front-swoosh { position: absolute; left: 0; bottom: 0; width: 100%; height: 90px; }

  .card-label { position: absolute; top: 620px; font-size: 17px; color: var(--label); letter-spacing: 0.3px; }
  .card-label--back { left: 66px; }
  .card-label--front { left: 692px; }
</style>
</head>
<body>
<main class="sheet">
  <h1 class="sheet-title">SUNNY DOODLES _BIZ CARD PHASE1 - 7/06/2011</h1>
  <div class="sheet-rule"></div>

  <section class="card card--back" aria-label="Business card back">
    <div class="back-artwork" role="img" aria-label="Faint yellow-toned character artwork filling the background"></div>
    <div class="card-edge"></div>
    <div class="contact">
      <p class="contact-name">Hana Melrose</p>
      <p class="contact-role">Artist</p>
      <p class="contact-line contact-phone"><b>Telephone:</b> 0432 918 246</p>
      <p class="contact-line contact-email"><b>email:</b> hana@sunnydoodles.com.au</p>
      <p class="contact-line contact-web">www.sunnydoodles.com.au</p>
    </div>
    <div class="back-brand">
      <span class="brand-dot"></span>
      <p class="back-brand-name">Sunny<br>Doodles</p>
    </div>
    <p class="back-tagline">Face Painting Designs</p>
  </section>

  <section class="card card--front" aria-label="Business card front">
    <div class="photo-strip">
      <div class="photo photo--one" role="img" aria-label="Photo of a child with butterfly face paint"></div>
      <div class="photo photo--two" role="img" aria-label="Photo of a child with lion face paint"></div>
      <div class="photo photo--three" role="img" aria-label="Photo of a child with colourful mask face paint"></div>
    </div>
    <svg class="front-swoosh" viewBox="0 0 538 90" preserveAspectRatio="none" aria-hidden="true">
      <path d="M190 90 C 300 60, 420 40, 538 30 L538 90 Z" fill="var(--purple-soft)"/>
      <path d="M250 90 C 340 72, 440 58, 538 52 L538 90 Z" fill="var(--purple)" opacity="0.75"/>
    </svg>
    <p class="front-tagline">Face Painting Designs</p>
    <div class="front-brand">
      <p class="front-brand-name">Sunny<br>Doodles</p>
    </div>
    <div class="card-edge"></div>
  </section>

  <p class="card-label card-label--back">BACK</p>
  <p class="card-label card-label--front">FRONT</p>
</main>
</body>
</html>
```